Bottlecap Decals Inc. NEED DESIGNS FOR THE HOLIDAY STICKERS

We need 6 designs for the HOLIDAY SET of Bottlecap Decals. I have attached some imagery that we like as well as the flagship pack of stickers that were also designed by you AWESOME DESIGNERS!! You are not limited to this imagery, it is only to show you what style we like but remember, YOU ARE THE ARTIST! Each design needs to have a "TO: & FROM:" for people to write in their name and the recipients name. We need designs for the following occasions:

1. HALLOWEEN
2. HAPPY HOLIDAYS (THANKSGIVING, CHRISTMAS, WINTER, LEAVES)
3. ST. PATRICK'S DAY
4. "LET'S CELEBRATE" PATRIOTIC THEME (JULY 4TH, VETERANS DAY, MEMORIAL DAY COMBINED)
5. HAPPY NEW YEAR
6. SUMMER THEME GENERIC

***these 6 designs must fit on one of die cut shapes which are included in the brief***

**PLEASE SUBMIT YOUR IDEA FOR AS MANY DESIGNS AS YOU CAN (PREFERABLY ALL 6). WE NEED 6 DESIGNS SO IF 4 OF YOURS ARE GOOD AND 2 OF ANOTHERS ARE GOOD, YOU WOULD WIN 1ST AND THEY WOULD WIN 2ND.

Font styles to use
Serif
Sans Serif
Decorative
Script

Requirements
Must have
• - lines for "to" and "from"
• - must fit on a die cut shape (provided)
• - must be FUN and colorful!!
Nice to have
• color, imagery, fun!

```html
<!DOCTYPE html>
<html lang="en">
<head>
<meta charset="utf-8">
<title>Happy New Year Gift Sticker</title>
<link rel="stylesheet" href="https://fonts.googleapis.com/css2?family=Berkshire+Swash&family=Pinyon+Script&family=Oswald:wght@600&display=swap">
<style>
  :root {
    --page: #ffffff;
    --gold: #d9ab3c;
    --gold-light: #f3da83;
    --gold-dark: #b58a2a;
    --linen: #e3ddd1;
    --rope-red: #c8111a;
    --title-red: #c8151c;
    --ink-grey: #8a8a8a;
    --rule-grey: #bdbdbd;
    --label-shadow: #a9a9a9;
  }
  html, body {
    margin: 0;
    padding: 0;
    width: 1200px;
    height: 1200px;
    overflow: hidden;
    background: var(--page);
  }
  .sticker {
    display: block;
    width: 1200px;
    height: 1200px;
  }
  .die-shadow { fill: var(--label-shadow); }
  .gold-edge { fill: url(#goldFoil); }
  .linen-field { fill: var(--linen); }
  .rope-frame {
    fill: none;
    stroke: var(--rope-red);
    stroke-width: 12;
    stroke-linejoin: round;
  }
  .message-window {
    fill: #ffffff;
    stroke: var(--rope-red);
    stroke-width: 16;
  }
  .ribbon-banner { fill: url(#ribbonFoil); }
  .foliage-spray { fill: var(--gold-light); opacity: 0.8; }
  .title-line {
    font-family: "Berkshire Swash", cursive;
    fill: var(--title-red);
    text-anchor: middle;
  }
  .title-happy { font-size: 112px; }
  .title-new-year { font-size: 116px; }
  .write-label {
    font-family: "Pinyon Script", cursive;
    font-size: 66px;
    fill: var(--ink-grey);
  }
  .write-line {
    stroke: var(--rule-grey);
    stroke-width: 2;
  }
  .year-mark {
    font-family: "Oswald", sans-serif;
    font-weight: 600;
    font-size: 124px;
    fill: var(--title-red);
    text-anchor: middle;
  }
</style>
</head>
<body>
<svg class="sticker" viewBox="0 0 1500 1500" xmlns="http://www.w3.org/2000/svg" aria-labelledby="stickerTitle">
  <title id="stickerTitle">Happy New Year 2017 gift sticker with from and to lines</title>
  <defs>
    <linearGradient id="goldFoil" x1="0" y1="0" x2="1" y2="1">
      <stop offset="0" stop-color="#f6e08d"/>
      <stop offset="0.45" stop-color="#d9ab3c"/>
      <stop offset="1" stop-color="#b98c2c"/>
    </linearGradient>
    <linearGradient id="ribbonFoil" x1="0" y1="0" x2="1" y2="0">
      <stop offset="0" stop-color="#b8832f"/>
      <stop offset="0.5" stop-color="#d8b24a"/>
      <stop offset="1" stop-color="#c9a23d"/>
    </linearGradient>
  </defs>

  <g class="label-body">
    <path class="die-shadow" transform="translate(4 8)"
      d="M465 300 Q760 100 1055 300 L1055 325 Q1060 430 1170 435 L1170 1005 Q1060 1010 1055 1140 Q760 1325 465 1140 Q460 1010 345 1005 L345 435 Q460 430 465 325 Z"/>
    <path class="gold-edge"
      d="M465 300 Q760 100 1055 300 L1055 325 Q1060 430 1170 435 L1170 1005 Q1060 1010 1055 1140 Q760 1325 465 1140 Q460 1010 345 1005 L345 435 Q460 430 465 325 Z"/>
    <path class="linen-field"
      d="M488 318 Q760 138 1032 318 L1032 338 Q1040 448 1148 456 L1148 984 Q1040 992 1032 1125 Q760 1295 488 1125 Q480 992 367 984 L367 456 Q480 448 488 338 Z"/>
    <path class="rope-frame"
      d="M500 326 Q760 156 1020 326 L1020 344 Q1030 458 1138 468 L1138 972 Q1030 982 1020 1118 Q760 1280 500 1118 Q490 982 378 972 L378 468 Q490 458 500 344 Z"/>
  </g>

  <path class="message-window"
    d="M790 350 C900 345 1000 390 1055 480 C1095 560 1090 680 1060 760 C1040 840 1000 900 900 930 C800 960 650 950 560 880 C480 820 470 720 478 600 C488 470 560 380 660 360 C710 350 750 352 790 350 Z"/>

  <path class="ribbon-banner" role="img" aria-label="Gold foil ribbon banner scattered with white snowflakes"
    d="M440 815 L510 830 L505 880 L565 900 Q790 940 1000 895 L1010 860 L1070 820 L1115 900 L1060 910 L1040 960 Q790 1010 540 975 L490 965 L480 920 L400 890 Z"/>

  <ellipse class="foliage-spray" role="img" aria-label="Gold leaf sprig" cx="520" cy="1000" rx="70" ry="38"/>
  <ellipse class="foliage-spray" role="img" aria-label="Gold leaf sprig" cx="1030" cy="930" rx="55" ry="70"/>
  <ellipse class="foliage-spray" role="img" aria-label="Gold star sprig" cx="450" cy="600" rx="50" ry="55"/>

  <text class="title-line title-happy" x="782" y="535">Happy</text>
  <text class="title-line title-new-year" x="785" y="665">New Year</text>

  <text class="write-label" x="570" y="780">from:</text>
  <line class="write-line" x1="555" y1="790" x2="975" y2="790"/>
  <text class="write-label" x="595" y="866">to:</text>
  <line class="write-line" x1="595" y1="878" x2="915" y2="878"/>

  <text class="year-mark" x="760" y="1158">2017</text>
</svg>
</body>
</html>
```